Kellwood Build, Carpentry Services

Business card for carpentry business in the Sunshine Coast.

Business card layout required using logo provided - provided both PDF copy and AI. Please let me know if you would like a the files for the logo symbol and text by itself.

Business Colours are grey, blue and white. The font colours codes for this design are Blue Hex # 00B4E6 and Hex # 39393B for the gray colour.

FYI font for logo is Gotham Bold.

Preference for a clean and striking layout that is simple and elegant.

Target Market(s)

Young Families, retirees, young couples requiring assistance with small to medium works/renovations on the Sunshine Coast.

Industry/Entity Type

Construction

Contact Information for Business Card

Dean Kellwood
Carpenter
0489305627
dean@kellwoodbuild.com.au
Palmvale, Coral Coast
RHPA Licensed Carpenter (In smaller font)

Font styles to use
Sans Serif

Colors

Designer to choose colors to be used in the design.

Requirements
Must have
• Logo provided must appear on the card, preferably on one side of the card by itself with the text on the alternate side
Nice to have
• Text on the other side of card, maybe grey background and white font here but happy for the designer to provide ideas here.
Should not have
• Use of other colours, other than the ones provided - white, grey and blue. Black optional.

```html
<!DOCTYPE html>
<html lang="en">
<head>
<meta charset="utf-8">
<title>Kellwood Build – Business Card</title>
<link href="https://fonts.googleapis.com/css2?family=Montserrat:wght@400;500;700&display=swap" rel="stylesheet">
<style>
  :root {
    --backdrop: #262628;
    --card-grey: #39393b;
    --brand-blue: #00b4e6;
    --white: #ffffff;
    --silver: #d6d6d8;
    --soft-white: #e9e9ea;
  }
  * { margin: 0; padding: 0; box-sizing: border-box; }
  html, body {
    width: 1200px; height: 895px; overflow: hidden;
    background: var(--backdrop);
    font-family: "Montserrat", Arial, sans-serif;
  }
  .canvas { position: relative; width: 1200px; height: 895px; }

  .card {
    position: absolute;
    width: 580px; height: 331px;
    background: var(--card-grey);
    border-bottom: 4px solid var(--brand-blue);
    box-shadow: 0 14px 30px rgba(0,0,0,0.45);
  }
  .card--front { left: 80px; top: 70px; }
  .card--back  { left: 540px; top: 490px; }

  .brand {
    position: absolute;
    display: flex; align-items: center;
  }
  .brand__mark { flex: none; }
  .brand__name {
    font-weight: 700; letter-spacing: 0.04em; text-transform: uppercase;
    white-space: nowrap;
  }

  /* Front: brand alone, centred */
  .card--front .brand { left: 50%; top: 50%; transform: translate(-50%, -50%); gap: 14px; }
  .card--front .brand__mark { background: var(--silver); width: 40px; height: 40px; }
  .card--front .brand__name { color: var(--silver); font-size: 38px; }

  /* Back: brand left, contact right */
  .card--back .brand { left: 36px; top: 186px; gap: 10px; }
  .card--back .brand__mark { background: var(--brand-blue); width: 20px; height: 20px; }
  .card--back .brand__name { color: var(--brand-blue); font-size: 19px; }

  .divider {
    position: absolute; left: 300px; top: 60px;
    width: 1px; height: 190px; background: var(--soft-white); opacity: 0.7;
  }
  .contact { position: absolute; left: 322px; top: 62px; color: var(--white); }
  .contact__name {
    color: var(--brand-blue); font-weight: 700; font-size: 20px;
    text-transform: uppercase; letter-spacing: 0.01em;
  }
  .contact__role { font-size: 14px; font-weight: 500; margin-top: 2px; }
  .contact__list { list-style: none; margin-top: 30px; }
  .contact__item {
    display: flex; align-items: center; gap: 10px;
    font-size: 13px; line-height: 1; margin-bottom: 11px;
  }
  .contact__icon { width: 13px; height: 13px; flex: none; }
  .licence {
    position: absolute; right: 40px; bottom: 28px;
    color: var(--soft-white); font-size: 11.5px; letter-spacing: 0.03em;
  }
</style>
</head>
<body>
<main class="canvas">

  <section class="card card--front" aria-label="Card front">
    <div class="brand">
      <span class="brand__mark"></span>
      <span class="brand__name">Kellwood Build</span>
    </div>
  </section>

  <section class="card card--back" aria-label="Card back">
    <div class="brand">
      <span class="brand__mark"></span>
      <span class="brand__name">Kellwood Build</span>
    </div>

    <div class="divider"></div>

    <div class="contact">
      <h1 class="contact__name">Dean Kellwood</h1>
      <p class="contact__role">Carpenter</p>
      <ul class="contact__list">
        <li class="contact__item">
          <svg class="contact__icon" viewBox="0 0 24 24" aria-hidden="true"><path fill="#00b4e6" d="M6.6 10.8a15.1 15.1 0 0 0 6.6 6.6l2.2-2.2c.3-.3.7-.4 1-.2 1.1.4 2.3.6 3.6.6.6 0 1 .4 1 1V20c0 .6-.4 1-1 1A17 17 0 0 1 3 4c0-.6.4-1 1-1h3.5c.6 0 1 .4 1 1 0 1.3.2 2.5.6 3.6.1.3 0 .7-.2 1z"/></svg>
          0489305627
        </li>
        <li class="contact__item">
          <svg class="contact__icon" viewBox="0 0 24 24" aria-hidden="true"><path fill="#00b4e6" d="M2 5h20v14H2zm2 2v.5l8 5 8-5V7l-8 5z"/></svg>
          dean@kellwoodbuild.com.au
        </li>
        <li class="contact__item">
          <svg class="contact__icon" viewBox="0 0 24 24" aria-hidden="true"><path fill="none" stroke="#00b4e6" stroke-width="2" d="M12 22s7-7 7-12a7 7 0 0 0-14 0c0 5 7 12 7 12z"/><circle cx="12" cy="10" r="2.5" fill="none" stroke="#00b4e6" stroke-width="2"/></svg>
          Palmvale, Coral Coast
        </li>
      </ul>
    </div>

    <p class="licence">RHPA Licensed Carpenter</p>
  </section>

</main>
</body>
</html>
```